New therapy private practice needs a 2 sided postcard announcing location and services

We need a postcard sized card that is TWO SIDED and shares our new location and services offered. (new location is 3840. W. 58th #2200 in Tulsa, OK 74129) Name of the therapy business is "Calm Harbor Counseling". Services offered include individual, marriage, family and group counseling. My phone number to place on the card is (918) 555-0148 and someone can call to schedule a free 20 minute consultation at that number.

These cards will also be mailed in an enclosed envelope or placed in welcome baskets as a marketing tool with possible referral sources like churches, doctors, and lawyers. (That means there does not have to be a space for an address or stamp to mail to. Full use of both sides of the card is important) We would like to see designs that use softer colors such as blue, purples, or greens. The final design should communicate a feeling of peace and hope and a sense of freshness and approachability. Incorporating a tag line such as..... "where you'll find hope!" would be good. My website is www.calmharborcare.example and extra info about my practice is on there. It is important my credentials are listed on the postcard. Dana Ruth Pell, LPC-S, LMFT

I am not looking for a bunch of "box looking pictures". The pictures I am uploading are for ideas, although my logo and picture should be used. I like the type of picture I have on my homepage of my website with the quote "Let your hopes, not your fears shape your future"

Target Market(s)

Primarily women and couples looking for counseling for relationships, anxiety, depression, or life transitions.

Font styles to use
Serif
Script

Colors
3276b5
85acd3
86cfc6
33b8a4
cadf82
876aae
9bcb3c

Requirements
Must have
• My picture, address, website, and phone number as well as my logo.
• Address is: 3840 W. 58th Street #2200 Tulsa, OK 74129
• Web: www.calmharborcare.example
• Email: dana@calmharborcare.example
• Phone: (918) 555-0148
• "Hope anchors the soul" - Heb. 6:19
• On my website, I have a 2 minute video of myself. This may be helpful to watch in getting a "feel" for my counseling practice.
• Services Provided: ANXIETY | DEPRESSION | LIFE TRANSITIONS | MARRIAGE COUNSELING | SEPARATION AND DIVORCE | WOMEN’S ISSUES | ADDICTIONS AND INFIDELITY | PARENT/CHILD RELATIONSHIPS | FAMILY CONFLICT | TRAUMA/GRIEF AND LOSS
Nice to have
• A combination of print and script would be nice. A feeling of tranquility and hope
• I would like to have the statement at the bottom of the card.... " It is my desire for you to discover that no matter the situation you are currently going through….. there’s hope!"
• It would also be nice to have a small area that says: Dana is a graduate of Western Lakeview College and has been in private practice for 11 years. She is a regular monthly co-host on the Meadow Broadcast Group at 88.3 FM
Should not have
• Heavy bold or abrasive feel

```html
<!DOCTYPE html>
<html lang="en">
<head>
<meta charset="utf-8">
<title>Calm Harbor Counseling – Postcard</title>
<link rel="stylesheet" href="https://fonts.googleapis.com/css2?family=Fraunces:ital,opsz,wght@0,9..144,400;0,9..144,600;1,9..144,400&family=Montserrat:wght@400;500;600&display=swap">
<style>
  :root{
    --page:#ffffff;
    --green:#3d8500;
    --green-soft:#7fb65a;
    --slate:#4f5a7e;
    --blue:#436a8d;
    --ink:#111111;
    --white:#ffffff;
    --autumn-a:#8c6a3e;
    --autumn-b:#c79a5a;
    --autumn-c:#5f6b45;
  }
  *{box-sizing:border-box;margin:0;padding:0}
  html,body{width:1200px;height:724px;overflow:hidden;background:var(--page)}
  body{position:relative;font-family:"Montserrat",Arial,sans-serif;color:var(--ink)}
  .card{position:absolute;top:200px;width:479px;height:369px;overflow:hidden;background:var(--white)}
  .card--front{left:103px}
  .card--back{left:626px}
  .photo{position:absolute}

  /* front */
  .front-photo{inset:0;background:
    radial-gradient(ellipse at 70% 35%, #d7b89a 0 18%, transparent 40%),
    linear-gradient(160deg,var(--autumn-c) 0%,var(--autumn-a) 45%,var(--autumn-b) 75%,#9c7a48 100%)}
  .intro-panel{position:absolute;left:44px;top:44px;width:168px;height:280px;background:var(--white);padding:17px 12px 0 14px}
  .brand{display:flex;align-items:center;gap:6px;height:48px}
  .brand__dot{width:18px;height:18px;border-radius:50%;background:var(--green);flex:none}
  .brand__name{font-family:"Fraunces",Georgia,serif;font-size:13px;line-height:1.1;color:var(--green)}
  .intro-panel__headline{margin-top:20px;font-size:12.6px;line-height:16.4px;font-weight:400}
  .intro-panel__rule{width:76px;height:2px;background:var(--green-soft);margin:5px 0 12px}
  .intro-panel__body{font-family:"Fraunces",Georgia,serif;font-style:italic;font-size:8.6px;line-height:14.5px}
  .quote-frame{position:absolute;left:265px;top:42px;width:162px;height:196px;border:1.5px solid var(--white);text-align:center;color:var(--white)}
  .quote-frame__mark{display:block;margin:26px auto 4px;width:26px;height:22px}
  .quote-frame__text{font-family:"Fraunces",Georgia,serif;font-style:italic;font-size:16px;line-height:24.5px}
  .info-band{position:absolute;left:212px;top:280px;width:267px;height:89px;background:var(--green);color:var(--white);padding:16px 0 0 54px}
  .info-band__name{font-family:"Fraunces",Georgia,serif;font-weight:600;font-size:10px;margin-bottom:6px}
  .info-band__line{font-size:7.3px;line-height:10.8px}
  .badge{position:absolute;width:54px;height:54px;border-radius:50%;display:flex;align-items:center;justify-content:center;text-align:center;color:var(--white);font-weight:600;font-size:8.6px;line-height:11px}
  .badge--location{left:185px;top:253px;background:var(--slate)}

  /* back */
  .about-panel{position:absolute;left:0;top:0;width:291px;height:245px;background:var(--blue);color:var(--white);padding:47px 0 0 39px}
  .about-panel__greeting{font-size:12.5px;font-weight:400}
  .about-panel__greeting strong{font-weight:600}
  .about-panel__text{margin-top:10px;width:205px;font-size:8.4px;line-height:14px}
  .services{display:flex;gap:13px;margin-top:14px;font-size:6.9px;line-height:11px;list-style:none}
  .services ul{list-style:none}
  .photo--mountain{left:291px;top:0;width:188px;height:123px;background:linear-gradient(160deg,#8a8f8a,#5e6a5c 55%,#3f3a30)}
  .photo--couple{left:291px;top:123px;width:188px;height:122px;background:linear-gradient(120deg,#7d7e80,#6a4a36 50%,#b59a80)}
  .photo--office{left:0;top:245px;width:213px;height:124px;background:linear-gradient(180deg,#b9b2a6,#8d9aa3 45%,#a79886)}
  .photo--portrait{left:247px;top:79px;width:88px;height:88px;border-radius:50%;background:linear-gradient(150deg,#d8b25a,#9c6a4a 60%,#5b2d3f)}
  .badge--contact{left:186px;top:218px;background:var(--green)}
  .contact-block{position:absolute;left:255px;top:262px;width:215px}
  .contact-block__lead{font-family:"Fraunces",Georgia,serif;font-weight:600;font-size:9.4px;line-height:13.7px}
  .contact-block__details{margin-top:8px;font-size:7px;line-height:10.8px}
  .brand--back{position:absolute;left:388px;top:317px;height:auto;gap:4px}
  .brand--back .brand__dot{width:13px;height:13px}
  .brand--back .brand__name{font-size:9.5px}
</style>
</head>
<body>
  <section class="card card--front">
    <div class="photo front-photo" role="img" aria-label="Young woman standing on an autumn park path with fallen leaves"></div>
    <div class="intro-panel">
      <div class="brand"><span class="brand__dot"></span><span class="brand__name">Calm Harbor<br>Counseling</span></div>
      <h1 class="intro-panel__headline">Today you are one step closer to finding your sense of hope, purpose, and fulfillment!</h1>
      <div class="intro-panel__rule"></div>
      <p class="intro-panel__body">Enlisting the help of a<br>professional can provide<br>a fresh perspective on a<br>difficult problem or point<br>you in the direction of a<br>positive solution.</p>
    </div>
    <blockquote class="quote-frame">
      <svg class="quote-frame__mark" viewBox="0 0 26 22" aria-hidden="true"><path fill="#3d8500" d="M1 0h10v10c0 6-3 10-9 12l-1-3c3-1 5-4 5-7H1zM15 0h10v10c0 6-3 10-9 12l-1-3c3-1 5-4 5-7h-5z"/></svg>
      <p class="quote-frame__text">Let your Hopes,<br>not your hurts,<br>shape your<br>future.</p>
    </blockquote>
    <div class="info-band">
      <p class="info-band__name">Calm Harbor Counseling</p>
      <p class="info-band__line">3840 W. 58th #2200 Tulsa, OK 74129</p>
      <p class="info-band__line">Call: (918) 555-0148</p>
      <p class="info-band__line">calmharborcare.example</p>
      <p class="info-band__line">dana@calmharborcare.example</p>
    </div>
    <div class="badge badge--location">New<br>Location</div>
  </section>

  <section class="card card--back">
    <div class="about-panel">
      <h2 class="about-panel__greeting">Hello! I am <strong>Dana Ruth Pell</strong></h2>
      <p class="about-panel__text">In 2007, I began my private practice and have been privileged to work with adolescents, individuals, couples, families, and groups focusing on a range of issues including:</p>
      <div class="services">
        <ul><li>- Anxiety</li><li>- Depression</li><li>- Life Transitions</li><li>- Marriage Counseling</li><li>- Separation And Divorce</li></ul>
        <ul><li>- Women's Issues</li><li>- Addictions And Infidelity</li><li>- Parent/Child Relationships</li><li>- Family Conflict</li><li>- Trauma/Grief And Loss</li></ul>
      </div>
    </div>
    <div class="photo photo--mountain" role="img" aria-label="Person sitting on a rock overlooking misty mountain cliffs"></div>
    <div class="photo photo--couple" role="img" aria-label="Couple embracing outdoors above a town"></div>
    <div class="photo photo--office" role="img" aria-label="Calm counseling office with sofas, blue pillows and curtains"></div>
    <div class="photo photo--portrait" role="img" aria-label="Portrait of the counselor in front of autumn foliage"></div>
    <div class="badge badge--contact">Contact<br>Me</div>
    <div class="contact-block">
      <p class="contact-block__lead">You can contact me at my Tulsa office<br>for an initial session or call to schedule a<br>Free 20 minute consultation.</p>
      <div class="contact-block__details">
        <p>3840 W. 58th #2200 Tulsa, OK 74129</p>
        <p>Call: (918) 555-0148</p>
        <p>calmharborcare.example</p>
        <p>dana@calmharborcare.example</p>
      </div>
    </div>
    <div class="brand brand--back"><span class="brand__dot"></span><span class="brand__name">Calm Harbor</span></div>
  </section>
</body>
</html>
```